4 x Designs Required

Hi There,
I require 4 x different designs to be made for 4 new brands of mine however they can be quite interchangeable. HR Plinkr and Marketing Plinkr can be similar just with a difference in colour. The same goes for the Bulletin brands. This means there are ultimately two designs that need perfecting.

There must be a click here CTA on the banner somewhere. :-)

I require the banners in 728x90 format and 960x90 please.

Please use strap lines on the banners such as:
Essential Whitepapers for HR Professionals
Essential Whitepapers for Marketing Professionals
Your No.1 Whitepaper Resource

The brand names:
HR Plinkr
Marketing Plinkr
HR Dispatchly
Marketing Dispatchly

Examples attached.

```html
<!DOCTYPE html>
<html lang="en">
<head>
<meta charset="utf-8">
<title>Whitepaper Brand Banners</title>
<link rel="stylesheet" href="https://fonts.googleapis.com/css2?family=Bebas+Neue&family=Poppins:wght@600;700&display=swap">
<style>
  :root {
    --page-bg: #e6e7e9;
    --strap-ink: #2b2f3a;
    --strap-light: #ffffff;
    --logo-ink: #ffffff;
    --btn-cyan: #44d2ea;
    --btn-cyan-ink: #10324a;
    --btn-mauve: #8a4565;
    --btn-magenta: #8c1652;
    --btn-lime: #a3d640;
    --btn-lime-ink: #1f3a0c;
    --btn-light-ink: #ffffff;
  }
  * { margin: 0; padding: 0; box-sizing: border-box; }
  html, body { width: 1200px; height: 786px; overflow: hidden; background: var(--page-bg); }
  .canvas { position: relative; width: 1200px; height: 786px; }

  .banner {
    position: absolute;
    width: 991px;
    height: 123px;
    overflow: hidden;
    box-shadow: 0 2px 8px rgba(0, 0, 0, 0.28);
  }
  .banner--hr-plinkr { left: 122px; top: 76px; }
  .banner--mkt-plinkr { left: 114px; top: 229px; }
  .banner--hr-dispatchly { left: 107px; top: 374px; }
  .banner--mkt-dispatchly { left: 107px; top: 540px; }

  .banner__bg { position: absolute; inset: 0; width: 100%; height: 100%; }

  .banner__logo,
  .banner__strap,
  .banner__cta { position: absolute; top: 50%; transform: translateY(-50%); white-space: nowrap; }

  .banner__logo { color: var(--logo-ink); line-height: 1; }
  .banner__logo--sans { font-family: "Poppins", sans-serif; font-weight: 700; font-size: 44px; letter-spacing: -0.5px; }
  .banner__logo--condensed { font-family: "Bebas Neue", sans-serif; font-size: 40px; }

  .banner__strap {
    font-family: "Bebas Neue", sans-serif;
    font-size: 30px;
    color: var(--strap-ink);
    line-height: 1;
  }
  .banner__strap--light { color: var(--strap-light); }
  .banner__strap--compact { font-size: 27px; }

  .banner__cta {
    font-family: "Poppins", sans-serif;
    font-weight: 600;
    font-size: 14px;
    height: 27px;
    width: 105px;
    border-radius: 14px;
    display: flex;
    align-items: center;
    justify-content: center;
    text-decoration: none;
    box-shadow: 0 1px 3px rgba(0, 0, 0, 0.25);
  }
  .banner__cta--large {
    top: 72px;
    transform: none;
    width: 150px;
    height: 38px;
    border-radius: 19px;
    font-size: 18px;
  }
  .cta--cyan { background: var(--btn-cyan); color: var(--btn-cyan-ink); }
  .cta--mauve { background: var(--btn-mauve); color: var(--btn-light-ink); }
  .cta--magenta { background: var(--btn-magenta); color: var(--btn-light-ink); }
  .cta--lime { background: var(--btn-lime); color: var(--btn-lime-ink); }
</style>
</head>
<body>
<main class="canvas">

  <section class="banner banner--hr-plinkr">
    <svg class="banner__bg" viewBox="0 0 991 123" preserveAspectRatio="none" aria-hidden="true">
      <defs>
        <linearGradient id="teal-base" x1="0" x2="1" y1="0" y2="0">
          <stop offset="0" stop-color="#0a3a58"/>
          <stop offset="0.3" stop-color="#1e7a9e"/>
          <stop offset="0.55" stop-color="#9eeaf6"/>
          <stop offset="0.78" stop-color="#3aa9d4"/>
          <stop offset="1" stop-color="#0d3f66"/>
        </linearGradient>
      </defs>
      <rect width="991" height="123" fill="url(#teal-base)"/>
      <polygon points="420,0 700,0 560,123 380,123" fill="#ffffff" opacity="0.18"/>
      <polygon points="560,0 991,60 991,0" fill="#0b4a78" opacity="0.35"/>
      <polygon points="0,123 300,40 360,123" fill="#06304a" opacity="0.3"/>
    </svg>
    <div class="banner__logo banner__logo--sans" style="left:24px;">HR Plinkr</div>
    <div class="banner__strap" style="left:321px;">Essential Whitepapers for HR Professionals</div>
    <a class="banner__cta cta--cyan" href="#" style="left:845px;">click here</a>
    <a class="banner__cta banner__cta--large cta--cyan" href="#" style="left:622px;">click here</a>
  </section>

  <section class="banner banner--mkt-plinkr">
    <svg class="banner__bg" viewBox="0 0 991 123" preserveAspectRatio="none" aria-hidden="true">
      <defs>
        <linearGradient id="mauve-base" x1="0" x2="1" y1="0" y2="0">
          <stop offset="0" stop-color="#5b4352"/>
          <stop offset="0.35" stop-color="#7a4a64"/>
          <stop offset="0.55" stop-color="#a85a84"/>
          <stop offset="0.8" stop-color="#6e3a55"/>
          <stop offset="1" stop-color="#4a2a3c"/>
        </linearGradient>
      </defs>
      <rect width="991" height="123" fill="url(#mauve-base)"/>
      <polygon points="400,0 640,0 520,123 360,123" fill="#ffffff" opacity="0.1"/>
      <polygon points="600,0 991,0 991,90" fill="#3e2232" opacity="0.3"/>
      <polygon points="0,0 260,0 120,123 0,123" fill="#8a7080" opacity="0.2"/>
    </svg>
    <div class="banner__logo banner__logo--condensed" style="left:18px;">Marketing Plinkr</div>
    <div class="banner__strap banner__strap--light" style="left:307px;">Essential Whitepapers for Marketing Professionals</div>
    <a class="banner__cta cta--mauve" href="#" style="left:872px;">click here</a>
  </section>

  <section class="banner banner--hr-dispatchly">
    <svg class="banner__bg" viewBox="0 0 991 123" preserveAspectRatio="none" aria-hidden="true">
      <defs>
        <linearGradient id="sunset-base" x1="0" x2="1" y1="0" y2="0">
          <stop offset="0" stop-color="#6e1240"/>
          <stop offset="0.25" stop-color="#c8204e"/>
          <stop offset="0.42" stop-color="#f39a1c"/>
          <stop offset="0.55" stop-color="#fde07a"/>
          <stop offset="0.75" stop-color="#e4661c"/>
          <stop offset="1" stop-color="#8a1a12"/>
        </linearGradient>
      </defs>
      <rect width="991" height="123" fill="url(#sunset-base)"/>
      <polygon points="420,0 640,0 560,123 400,123" fill="#ffffff" opacity="0.2"/>
      <polygon points="660,0 991,0 991,123 820,123" fill="#7a1010" opacity="0.25"/>
      <polygon points="200,123 380,0 460,0 300,123" fill="#b01a4a" opacity="0.25"/>
    </svg>
    <div class="banner__logo banner__logo--sans" style="left:24px;">HR Dispatchly</div>
    <div class="banner__strap" style="left:357px;">Essential Whitepapers for HR Professionals</div>
    <a class="banner__cta cta--magenta" href="#" style="left:866px;">click here</a>
  </section>

  <section class="banner banner--mkt-dispatchly">
    <svg class="banner__bg" viewBox="0 0 991 123" preserveAspectRatio="none" aria-hidden="true">
      <defs>
        <linearGradient id="lime-base" x1="0" x2="1" y1="0" y2="0">
          <stop offset="0" stop-color="#2f5a12"/>
          <stop offset="0.3" stop-color="#7fb430"/>
          <stop offset="0.55" stop-color="#e6f59c"/>
          <stop offset="0.78" stop-color="#84bb30"/>
          <stop offset="1" stop-color="#2f6212"/>
        </linearGradient>
      </defs>
      <rect width="991" height="123" fill="url(#lime-base)"/>
      <polygon points="420,0 660,0 580,123 400,123" fill="#ffffff" opacity="0.2"/>
      <polygon points="700,0 991,0 991,123" fill="#2a5a10" opacity="0.3"/>
      <polygon points="0,123 320,30 360,123" fill="#1f4a0a" opacity="0.25"/>
    </svg>
    <div class="banner__logo banner__logo--condensed" style="left:26px;">Marketing Dispatchly</div>
    <div class="banner__strap banner__strap--compact" style="left:374px;">Essential Whitepapers for Marketing Professionals</div>
    <a class="banner__cta cta--lime" href="#" style="left:869px;">click here</a>
  </section>

</main>
</body>
</html>
```